Take-away menu design

We need a double-sided menu brochure designed, the measurements are 195mmx280mm. We have all the details provided for you such as color RGB, content, fonts, logo and the precedent. We would like our content to be implemented into the precedent menu provided.

Industry/Entity Type

Fish and Chips

Font styles to use
Other font styles liked:
• Museo Slab 300, Kauvita Greek Bold Regular

```html
<!DOCTYPE html>
<html lang="en">
<head>
<meta charset="utf-8">
<title>Tide &amp; Tartare — Take-away Menu</title>
<link rel="stylesheet" href="https://fonts.googleapis.com/css2?family=Roboto+Slab:wght@300;400;800;900&family=Barlow+Semi+Condensed:wght@600;700&display=swap">
<style>
  :root{
    --ink:#231f20;
    --blue:#1a9be6;
    --paper:#ffffff;
    --muted:#3a3637;
  }
  *{box-sizing:border-box;margin:0;padding:0}
  html,body{width:836px;height:1200px;overflow:hidden;background:var(--paper)}
  body{position:relative;font-family:"Roboto Slab",serif;font-weight:300;color:var(--ink);font-size:12.4px}
  .masthead{position:absolute;left:0;top:0;width:836px;height:107px;background:var(--ink);display:flex;align-items:center;justify-content:center;gap:12px}
  .masthead .mark{width:14px;height:14px;background:var(--blue)}
  .masthead .brand{color:#fff;font-family:"Roboto Slab",serif;font-weight:300;font-size:23px;letter-spacing:.5px}
  .block{position:absolute}
  .col-left{left:30px;width:371px}
  .col-right{left:435px;width:371px}
  .bar{height:31px;background:var(--ink);color:#fff;font-family:"Barlow Semi Condensed",sans-serif;font-weight:700;font-size:16.5px;letter-spacing:.3px;display:flex;align-items:center;padding-left:8px}
  .bar .plus{color:var(--blue);margin:0 4px}
  .note{font-size:12.2px;line-height:12px;color:var(--muted)}
  .menu-list{list-style:none}
  .item{position:relative;border-top:2.6px solid var(--ink);height:32.8px;display:flex;align-items:center;padding-right:26px;white-space:nowrap}
  .menu-list.closed{border-bottom:2.6px solid var(--ink)}
  .item .name{color:var(--blue);font-weight:900}
  .item .plain-bold{font-weight:900}
  .price{position:absolute;right:0;top:7px;width:17px;height:17px;background:var(--blue);color:#fff;font-family:"Barlow Semi Condensed",sans-serif;font-weight:700;font-size:11.5px;display:flex;align-items:center;justify-content:center}
  .item.tall{height:auto;display:block;padding:6px 30px 8px 0;white-space:normal;line-height:15.2px}
  .item.tall .price{top:8px}
  .prep{display:flex;align-items:center;gap:10px;color:var(--muted)}
  .select{border:1px solid var(--ink);height:22px;width:180px;display:flex;align-items:center;padding-left:11px;gap:6px;color:var(--ink)}
  .select svg{width:8px;height:6px}
  .options{display:flex;gap:10px;font-size:10.4px;color:var(--muted);margin-left:67px;margin-top:6px}
  .options span{display:flex;align-items:center;gap:3px}
  .box{width:9px;height:9px;border:1px solid var(--ink);display:inline-block}
</style>
</head>
<body>
  <header class="masthead">
    <span class="mark"></span>
    <span class="brand">TIDE &amp; TARTARE</span>
  </header>

  <!-- Left column -->
  <section class="block col-left" style="top:119px">
    <h2 class="bar">FISH<span class="plus">+</span>CHIPS</h2>
    <p class="note" style="margin-top:12px">[Served with your choice of chips, tartare sauce &amp; lemon.]</p>
  </section>
  <ul class="block col-left menu-list closed" style="top:188px">
    <li class="item"><span><span class="name">Cod</span> &amp; chips (NZ, wild caught)</span><span class="price">15</span></li>
    <li class="item"><span><span class="name">Whiting</span> &amp; chips (QLD, wild caught, crumbed only)</span><span class="price">17</span></li>
    <li class="item"><span><span class="name">Flathead</span> &amp; chips (SA, wild caught, beer battered only)</span><span class="price">20</span></li>
    <li class="item"><span><span class="name">Snapper</span> &amp; chips (NT, wild caught)</span><span class="price">20</span></li>
    <li class="item"><span><span class="name">Barramundi</span> &amp; chips (NT, ocean farmed)</span><span class="price">20</span></li>
    <li class="item"><span><span class="name">Salmon</span> &amp; chips (TAS, ocean farmed)</span><span class="price">21</span></li>
    <li class="item"><span><span class="name">Crumbed Calamari</span> (8) &amp; chips</span><span class="price">15</span></li>
    <li class="item"><span><span class="name">Salt &amp; Pepper Calamari</span> (8) &amp; chips</span><span class="price">17</span></li>
    <li class="item"><span><span class="name">Crumbed Prawns</span> (5) &amp; chips</span><span class="price">28</span></li>
    <li class="item"><span><span class="name">BBQ Prawn Skewers</span> (5) &amp; chips</span><span class="price">28</span></li>
  </ul>
  <div class="block col-left" style="top:528px">
    <div class="prep">Made fresh to order
      <span class="select">Choose your preparation
        <svg viewBox="0 0 8 6"><path d="M0 0H8L4 6Z" fill="var(--blue)"/></svg>
      </span>
    </div>
    <div class="options">
      <span><i class="box"></i>GRILLED</span>
      <span><i class="box"></i>CRUMBED</span>
      <span><i class="box"></i>BEER BATTERED</span>
    </div>
  </div>

  <section class="block col-left" style="top:588px">
    <h2 class="bar">COOKED SEAFOOD PLATTERS</h2>
    <p class="note" style="margin-top:7px">[Cooked Seafood Platters include: whiting, calamari, salt &amp; pepper calamari, prawns, sea scallops, chips,<br>one of our freshly made salads, tartare sauce &amp; lemon.]</p>
  </section>
  <ul class="block col-left menu-list" style="top:678px">
    <li class="item"><span class="plain-bold">Cooked Platter for One</span><span class="price">26</span></li>
    <li class="item"><span class="plain-bold">Cooked Platter for Two</span><span class="price">51</span></li>
    <li class="item"><span class="plain-bold">Cooked Platter for Three</span><span class="price">76</span></li>
  </ul>
  <p class="block col-left note" style="top:777px">Our seafood platters are available crumbed only.</p>

  <section class="block col-left" style="top:808px">
    <h2 class="bar">STARTERS<span class="plus">+</span>SIDES</h2>
  </section>
  <ul class="block col-left menu-list" style="top:855px">
    <li class="item"><span>Crumbed Calamari (8)</span><span class="price">10</span></li>
    <li class="item"><span>Salt &amp; Pepper Calamari (8)</span><span class="price">12</span></li>
    <li class="item"><span>Crumbed Sea Scallop</span><span class="price">5</span></li>
    <li class="item"><span>Crumbed Prawn</span><span class="price">5</span></li>
    <li class="item"><span>BBQ Prawn Skewer</span><span class="price">5</span></li>
    <li class="item"><span>Onion Rings (8)</span><span class="price">10</span></li>
    <li class="item"><span>Popcorn Chicken</span><span class="price">10</span></li>
    <li class="item"><span>Potato Scallop</span><span class="price">4</span></li>
    <li class="item"><span>Grilled Halloumi (3 slices)</span><span class="price">12</span></li>
    <li class="item"><span>Fried Halloumi (3 slices, crumbed)</span><span class="price">12</span></li>
  </ul>

  <!-- Right column -->
  <section class="block col-right" style="top:119px">
    <h2 class="bar">SALADS</h2>
    <p class="note" style="margin-top:11px">[Freshly prepared to order using local produce.]</p>
  </section>
  <ul class="block col-right menu-list" style="top:188px">
    <li class="item tall" style="height:77px"><span class="name">Greek</span><br>Lettuce, cucumber, tomato, red onion, Kalamata olives, feta, Greek peppers, wild oregano, dressed in Greek extra virgin olive Oil vinaigrette.<span class="price">10</span></li>
    <li class="item tall" style="height:77px"><span class="name">Roast Pumpkin</span><br>Roast pumpkin, wild rocket, Parmigiano Reggiano, toasted pine nuts, dressed in Greek extra virgin olive oil &amp; vintage balsamic vinegar.<span class="price">10</span></li>
    <li class="item tall" style="height:61px"><span class="name">Slaw</span><br>Shredded red &amp; green cabbage, carrot, tossed in a light mayonnaise dressing.<span class="price">10</span></li>
    <li class="item tall"><span class="name">Asian Slaw</span><br>Shredded red &amp; green cabbage, carrot, spring onion, crispy noodles, sesame seeds, tossed in a sweet soy dressing.<span class="price">10</span></li>
  </ul>

  <section class="block col-right" style="top:491px"><h2 class="bar">CHIPS</h2></section>
  <ul class="block col-right menu-list" style="top:535px">
    <li class="item"><span>Chips GF</span><span class="price">6</span></li>
    <li class="item"><span>Beer Battered Chips</span><span class="price">8</span></li>
    <li class="item"><span>Sweet Potato Chips</span><span class="price">8</span></li>
  </ul>

  <section class="block col-right" style="top:643px"><h2 class="bar">SAUCES</h2></section>
  <ul class="block col-right menu-list" style="top:686px">
    <li class="item"><span>Tartare, Aioli, Tomato &amp; Chipotle Mayonnaise</span><span class="price">2</span></li>
  </ul>

  <section class="block col-right" style="top:729px"><h2 class="bar">BURGERS<span class="plus">+</span>TACOS</h2></section>
  <ul class="block col-right menu-list" style="top:772px">
    <li class="item tall" style="height:60px"><span class="name">Fish Burger</span> &amp; chips<br>Crumbed cod fillet, shredded lettuce, tomato &amp; tartare sauce in a toasted bun.<span class="price">16</span></li>
    <li class="item tall" style="height:62px"><span class="name">Fish Tacos</span> (3) &amp; chips<br>Beer battered cod, shredded red &amp; green cabbage, carrot, chipotle mayonnaise in soft flour tortillas.<span class="price">16</span></li>
    <li class="item tall" style="height:62px"><span class="name">Chicken Burger</span> &amp; chips<br>Grilled free range chicken tenders, shredded lettuce, tomato, cheese, avocado, aioli in a toasted bun.<span class="price">16</span></li>
    <li class="item tall"><span class="name">Steak Burger</span> &amp; chips<br>Grilled grass fed rib fillet, shredded lettuce, tomato, cheese, caramelised onion, BBQ sauce in a toasted bun.<span class="price">18</span></li>
  </ul>

  <section class="block col-right" style="top:1027px"><h2 class="bar">CHILDREN'S FISH<span class="plus">+</span>CHIPS</h2></section>
  <ul class="block col-right menu-list" style="top:1070px">
    <li class="item"><span><span class="name">Fish Fingers</span> (4) &amp; chips</span><span class="price">12</span></li>
    <li class="item"><span><span class="name">Crumbed Calamari</span> (4) &amp; chips</span><span class="price">12</span></li>
    <li class="item"><span><span class="name">Popcorn Chicken</span> &amp; chips</span><span class="price">12</span></li>
  </ul>
</body>
</html>
```